Lumora Works - Design & Marketing Website Re-branding

UPDATE:
We are working on finalizing our color palette but are hoping that the designers will guide us to the right choice of colors by looking at our color inspiration file that we just uploaded and lead us in the right direction.

-----

I am exploring new design inspiration for a re-branding of my website. My current website is old and outdated and I lack the time to design it myself in addition to the fact that I am my own worst client.

I do website design, development and marketing as well as some SEO consulting and business development for small to mid-size companies in a range of industries.

https://lumoraworks.example

I like clean modern designs without cartoon images. The brands I'm going after are looking for a professional look and feel. I need something that shows my many years of being in business that is very professional.

I prefer minimal use of color. Mostly black and white with maybe one or two other colors. I am open to the suggestions by the designer.

Target Market(s)

Small to mid-size companies

Industry/Entity Type

Website Design, SEO and Markeitng

Number of Pages Required

4 page

Font styles to use
Sans Serif

Requirements
Must have
• Must be clean, modern and professional - I am not a huge fan of a lot of color and I'm open to new color suggestions by the designer
Nice to have
• A good balance of whitespace to content and graphics
Should not have
• Please no people illustrations

```html
<!DOCTYPE html>
<html lang="en">
<head>
<meta charset="utf-8">
<title>Lumora Works — Website Design &amp; Marketing</title>
<link href="https://fonts.googleapis.com/css2?family=Montserrat:wght@400;500;600;700;800;900&display=swap" rel="stylesheet">
<style>
:root{
  --ink:#1d1a1f;
  --plum-deep:#2a0f28;
  --plum:#3d1538;
  --plum-mid:#5a2555;
  --accent:#7b3b76;
  --cta-a:#7a2f72;
  --cta-b:#4a1744;
  --grey-bg:#f4f3f4;
  --muted:#5c5860;
  --star:#f5b82e;
  --white:#ffffff;
}
*{box-sizing:border-box;margin:0;padding:0}
html,body{width:1200px;height:3610px;overflow:hidden}
body{font-family:"Montserrat",sans-serif;color:var(--ink);background:var(--white);position:relative}

/* Hero */
.hero{position:absolute;left:0;top:0;width:1200px;height:667px;background:var(--plum-deep);border-bottom-right-radius:150px;overflow:hidden}
.hero-photo{position:absolute;left:380px;top:0;width:820px;height:667px;
  background:radial-gradient(ellipse at 60% 45%,#6b5a5e 0%,#3d2e35 40%,transparent 75%),linear-gradient(90deg,var(--plum-deep) 0%,#3a2730 35%,#2e2228 100%)}
.brand{position:absolute;left:109px;top:22px;color:var(--white);font-weight:800;font-size:24px;letter-spacing:-.5px}
.brand span{display:inline-block;width:9px;height:9px;border-radius:50%;background:var(--accent);margin-left:3px}
.chat-link{position:absolute;left:950px;top:34px;color:var(--white);font-size:11px;display:flex;align-items:center;gap:7px}
.menu-btn{position:absolute;left:1049px;top:21px;width:42px;height:42px;border-radius:50%;background:var(--plum-mid);display:flex;align-items:center;justify-content:center}
.eyebrow{position:absolute;left:109px;top:191px;color:var(--white);font-size:12px;letter-spacing:1px;font-weight:500}
.hero-title{position:absolute;left:108px;top:220px;color:var(--white);font-weight:800;font-size:42px;line-height:44px;letter-spacing:.3px}
.hero-title i{font-style:normal;color:var(--accent)}
.hero-sub{position:absolute;left:109px;top:367px;color:var(--white);font-size:14px;line-height:18px;width:330px}
.btn{position:absolute;display:flex;align-items:center;justify-content:center;gap:6px;border-radius:22px;font-weight:700;font-size:11px;letter-spacing:.3px;text-transform:uppercase}
.btn-fill{background:var(--accent);color:var(--white)}
.btn-line{border:1.5px solid rgba(255,255,255,.7);color:var(--white)}

/* Section titles */
.sec-title{position:absolute;left:0;width:1200px;text-align:center;font-size:36px;font-weight:400;letter-spacing:.5px;color:var(--ink)}
.sec-title b{font-weight:800}
.sec-dot{position:absolute;left:596px;width:8px;height:8px;border-radius:50%;background:var(--accent)}

/* Services */
.service{position:absolute;top:833px;width:282px;height:472px;background:var(--white);border-bottom-right-radius:56px;box-shadow:0 14px 30px rgba(0,0,0,.09);overflow:hidden;text-align:center}
.service.is-dark{background:var(--plum);color:var(--white)}
.service-photo{height:235px}
.service-icon{position:absolute;left:107px;top:201px;width:68px;height:68px;border-radius:50%;background:var(--plum-mid);border:3px solid var(--white);display:flex;align-items:center;justify-content:center}
.is-dark .service-icon{background:var(--white);border-color:var(--plum)}
.service h3{margin-top:60px;font-size:16px;font-weight:400;letter-spacing:.4px}
.service h3 b{font-weight:800}
.service p{margin:14px auto 0;width:220px;font-size:12px;line-height:18px;color:var(--muted)}
.is-dark p{color:#e6dbe5}
.service .pill{margin:20px auto 0;width:200px;height:33px;border:2px solid var(--accent);border-radius:17px;display:flex;align-items:center;justify-content:center;font-size:9.5px;font-weight:700;color:var(--accent);letter-spacing:.3px}
.is-dark .pill{border-color:#7c4a78;color:var(--white)}

/* Reviews */
.reviews{position:absolute;left:0;top:1410px;width:1200px;height:546px;background:var(--grey-bg)}
.review{position:absolute;top:167px;width:294px;height:257px;background:var(--white);border-radius:6px;box-shadow:0 6px 18px rgba(0,0,0,.07);padding:22px 22px}
.reviewer{display:flex;align-items:center;gap:10px}
.avatar{width:54px;height:54px;border-radius:50%;border:3px solid var(--accent);background:linear-gradient(135deg,#c9b6bd,#8c7a80)}
.reviewer .name{font-size:12px;font-weight:600}
.stars{color:var(--star);font-size:13px;letter-spacing:1px;margin-top:3px}
.review p{margin-top:22px;font-size:10.5px;line-height:19px;color:var(--muted)}
.quote{position:absolute;right:20px;bottom:16px}
.dots{position:absolute;top:450px;left:570px;display:flex;gap:11px}
.dots span{width:8px;height:8px;border-radius:50%;background:#d6d2d6}
.dots span.on{background:var(--accent);width:10px;height:10px;margin-top:-1px}

/* CTA */
.cta{position:absolute;left:0;top:1956px;width:1200px;height:357px;background:linear-gradient(180deg,var(--cta-a),var(--cta-b))}
.cta h2{position:absolute;left:0;top:88px;width:1200px;text-align:center;color:var(--white);font-weight:800;font-size:48px;line-height:53px}
.cta .start{position:absolute;left:488px;top:221px;width:224px;height:44px;border-radius:22px;background:var(--white);color:var(--ink);font-weight:700;font-size:12px;display:flex;align-items:center;justify-content:center}

/* Values */
.intro{position:absolute;left:0;width:1200px;text-align:center;font-size:14px;line-height:19px;color:var(--ink)}
.value{position:absolute;top:2602px;width:266px;height:301px;border:1.5px solid #dcd8dc;background:var(--white);text-align:center}
.value.is-dark{background:var(--plum);border-color:var(--plum);color:var(--white);box-shadow:0 18px 30px rgba(0,0,0,.18)}
.value svg{margin-top:40px}
.value h3{margin-top:22px;font-size:16px;font-weight:700;letter-spacing:.4px}
.value p{margin:24px auto 0;width:200px;font-size:11.5px;line-height:17px;color:var(--muted)}
.value.is-dark p{color:#dacdd8}

/* Clients */
.clients{position:absolute;left:0;top:3011px;width:1200px;height:330px;background:var(--grey-bg)}
.client{position:absolute;top:104px;width:151px;height:79px;background:var(--white);display:flex;align-items:center;justify-content:center;gap:7px;font-size:17px;font-weight:700;color:#555}
.client i{display:inline-block;width:14px;height:14px;background:#777;border-radius:50%}

/* Footer */
.footer{position:absolute;left:0;top:3297px;width:1200px;height:313px;background:var(--plum-deep);border-top-left-radius:112px;color:var(--white)}
.contact{position:absolute;top:98px;display:flex;gap:12px;font-size:11px;line-height:15px}
.contact .lbl{text-transform:uppercase}
.social{position:absolute;left:905px;width:22px;height:22px;border-radius:50%;background:var(--white)}
.foot-brand{position:absolute;left:250px;top:166px;font-size:20px;font-weight:700;letter-spacing:-.3px}
.foot-link{position:absolute;top:172px;font-size:11px;letter-spacing:.3px}
.copy{position:absolute;left:0;top:276px;width:1200px;text-align:center;font-size:11px}
</style>
</head>
<body>

<header class="hero">
  <div class="hero-photo" role="img" aria-label="Photo of a team gathered around a desk reviewing work in a dim office"></div>
  <div class="brand">Lumora Works<span></span></div>
  <div class="chat-link">
    <svg width="13" height="12" viewBox="0 0 13 12"><path d="M1 2h8v5H4l-3 2z" fill="#fff"/><path d="M10 4h2v5l-2-1.5H6V8" fill="none" stroke="#fff"/></svg>
    Let's chat
  </div>
  <div class="menu-btn">
    <svg width="20" height="14" viewBox="0 0 20 14" fill="#fff"><circle cx="2" cy="2" r="1.5"/><circle cx="2" cy="7" r="1.5"/><circle cx="2" cy="12" r="1.5"/><rect x="6" y="1" width="13" height="2" rx="1"/><rect x="6" y="6" width="13" height="2" rx="1"/><rect x="6" y="11" width="13" height="2" rx="1"/></svg>
  </div>
  <div class="eyebrow">LUMORA WORKS &nbsp;. . .&nbsp; WELCOME</div>
  <h1 class="hero-title">EVERY BUSINESS<br>HAS A STORY<i>.</i> WE<br>HELP YOU TELL IT<i>.</i></h1>
  <p class="hero-sub">Compelling website experiences that elevate your business.</p>
  <div class="btn btn-fill" style="left:109px;top:435px;width:153px;height:40px">What we do</div>
  <div class="btn btn-line" style="left:278px;top:435px;width:151px;height:40px">
    <svg width="12" height="11" viewBox="0 0 13 12"><path d="M1 2h8v5H4l-3 2z" fill="#fff"/></svg>Let's chat
  </div>
</header>

<h2 class="sec-title" style="top:744px">OUR <b>SERVICES</b></h2>
<div class="sec-dot" style="top:792px"></div>

<article class="service" style="left:109px">
  <div class="service-photo" role="img" aria-label="Photo of a laptop on a desk showing a sign-up page" style="background:linear-gradient(160deg,#9aa3a8,#3f4a52)"></div>
  <div class="service-icon"><svg width="34" height="34" viewBox="0 0 34 34" fill="none" stroke="#fff" stroke-width="2.4" stroke-linecap="round"><path d="M17 5v24M6 17h22M17 5l-3 3M17 5l3 3M6 17l3-3M6 17l3 3M28 17l-3-3M28 17l-3 3"/></svg></div>
  <h3>WEBSITES <b>SIMPLIFIED</b></h3>
  <p>A complete end-to-end website subscription solution that propels your business forward.</p>
  <div class="pill">COMPLETE WEBSITE SOLUTION</div>
</article>

<article class="service is-dark" style="left:458px">
  <div class="service-photo" role="img" aria-label="Photo of a designer working at a desktop monitor with wireframes" style="background:linear-gradient(160deg,#c9a47a,#4a3626)"></div>
  <div class="service-icon"><svg width="34" height="34" viewBox="0 0 34 34" fill="none" stroke="#3d1538" stroke-width="2"><rect x="4" y="7" width="22" height="16" rx="1.5"/><path d="M11 28h8M15 23v5M20 4l8 8-5 1-4-4z"/></svg></div>
  <h3>CUSTOM <b>WEBSITE DESIGN</b></h3>
  <p>Blending the best principles of design, data and functionality to express your brand.</p>
  <div class="pill">DESIGN SERVICES</div>
</article>

<article class="service" style="left:807px">
  <div class="service-photo" role="img" aria-label="Photo of support staff with headsets working at computers" style="background:linear-gradient(160deg,#4d5866,#1e232b)"></div>
  <div class="service-icon"><svg width="34" height="34" viewBox="0 0 34 34" fill="none" stroke="#fff" stroke-width="2"><rect x="4" y="6" width="26" height="17" rx="1.5"/><path d="M12 28h10M17 23v5"/><circle cx="17" cy="14" r="4"/><path d="M17 8v2M17 18v2M11 14h2M21 14h2"/></svg></div>
  <h3>WEBSITE <b>SUPPORT</b></h3>
  <p>Reliable top tier CMS website support, maintenance and hosting.</p>
  <div class="pill">WEBSITE CARE</div>
</article>

<section class="reviews">
  <h2 class="sec-title" style="top:75px">OUR <b>REVIEWS</b></h2>
  <div class="sec-dot" style="top:124px"></div>

  <article class="review" style="left:132px">
    <div class="reviewer"><div class="avatar" role="img" aria-label="Reviewer portrait"></div><div><div class="name">Martin Oakes</div><div class="stars">★★★★★</div></div></div>
    <p>The team at Brightway Media are phenomenal.Ava,Lee,Nora,Tess and Max took my business to another level and exceeded my every expectation.I truly believe that if you are not [...]</p>
    <svg class="quote" width="52" height="30" viewBox="0 0 52 30" fill="#ececec"><path d="M0 30V14Q0 2 12 0v6q-5 2-5 8h7v16zM28 30V14q0-12 12-14v6q-5 2-5 8h7v16z"/></svg>
  </article>
  <article class="review" style="left:453px">
    <div class="reviewer"><div class="avatar" role="img" aria-label="Reviewer portrait"></div><div><div class="name">Dana Whitlow</div><div class="stars">★★★★★</div></div></div>
    <p>Positive: Professionalism Brightway Media are a comprehensive professional Media group that has been a great business partner. I can always trust their recommendations and ideas. They continually respond [...]</p>
    <svg class="quote" width="52" height="30" viewBox="0 0 52 30" fill="#ececec"><path d="M0 30V14Q0 2 12 0v6q-5 2-5 8h7v16zM28 30V14q0-12 12-14v6q-5 2-5 8h7v16z"/></svg>
  </article>
  <article class="review" style="left:774px">
    <div class="reviewer"><div class="avatar" role="img" aria-label="Reviewer portrait"></div><div><div class="name">Ruben Hale</div><div class="stars">★★★★★</div></div></div>
    <p>Positive: Professionalism, Quality, Responsiveness We have enjoyed a very professional experience utilizing Brightway Media for our digital marketing and website. The team is there to promote our business [...]</p>
    <svg class="quote" width="52" height="30" viewBox="0 0 52 30" fill="#ececec"><path d="M0 30V14Q0 2 12 0v6q-5 2-5 8h7v16zM28 30V14q0-12 12-14v6q-5 2-5 8h7v16z"/></svg>
  </article>

  <div class="dots"><span class="on"></span><span></span><span></span><span></span></div>
</section>

<section class="cta" role="img" aria-label="Purple-tinted photo of a team working together in an office">
  <h2>LET'S WORK<br>TOGETHER</h2>
  <div class="start">GET STARTED</div>
</section>

<h2 class="sec-title" style="top:2403px">WE CREATE WEBSITES <b>THAT INSPIRE</b></h2>
<p class="intro" style="top:2467px">We are a collaborative team of word nerds, choreographers of shapes &amp; ideas, ambassadors of data, content<br>warriors and inspirational conversationalists ready to help you no matter where you are in your journey.</p>
<p class="intro" style="top:2516px;font-weight:700;font-size:13px">We have a deep understanding of what it takes to grow a business and we collaborate with you every<br>step of the way from strategy to implementation and beyond.</p>

<article class="value" style="left:143px">
  <svg width="56" height="56" viewBox="0 0 56 56" fill="none" stroke="#5a2555" stroke-width="5"><path d="M28 6a22 22 0 0 1 21 15M50 34a22 22 0 0 1-19 16M23 50A22 22 0 0 1 6 32M7 22A22 22 0 0 1 22 7"/><path d="M18 22h20M18 28h20M18 34h20" stroke-width="4"/></svg>
  <h3>PROVEN PROCESS</h3>
  <p>We have carefully crafted each step in our process for successful outcomes.</p>
</article>
<article class="value is-dark" style="left:467px">
  <svg width="56" height="56" viewBox="0 0 56 56" fill="#fff"><circle cx="28" cy="10" r="7"/><circle cx="9" cy="44" r="7"/><circle cx="47" cy="44" r="7"/><path d="M14 30a16 16 0 0 1 6-13M42 30a16 16 0 0 0-6-13M20 50a16 16 0 0 0 16 0" fill="none" stroke="#fff" stroke-width="3"/></svg>
  <h3>CONNECTION</h3>
  <p>We take the time to truly listen and understand your audience and business needs.</p>
</article>
<article class="value" style="left:789px">
  <svg width="56" height="56" viewBox="0 0 56 56" fill="none" stroke="#5a2555" stroke-width="4"><circle cx="28" cy="28" r="18"/><circle cx="28" cy="28" r="9" fill="#5a2555"/><path d="M28 2v10M28 44v10M2 28h10M44 28h10"/></svg>
  <h3>EXCEEDING YOUR GOALS</h3>
  <p>We develop actionable strategies for success based on your unique goals.</p>
</article>

<section class="clients" aria-label="Clients">
  <div class="client" style="left:-104px"></div>
  <div class="client" style="left:112px"><i></i>Nordvale</div>
  <div class="client" style="left:278px">brightpath</div>
  <div class="client" style="left:443px"><i></i>LinkSphere</div>
  <div class="client" style="left:608px">Open Ladder</div>
  <div class="client" style="left:774px">Harbor Table</div>
  <div class="client" style="left:939px"><i></i>Keystone</div>
  <div class="client" style="left:1155px"></div>
</section>

<footer class="footer">
  <div class="contact" style="left:248px">
    <svg width="14" height="18" viewBox="0 0 14 18"><path d="M7 1a6 6 0 0 1 6 6c0 4-6 10-6 10S1 11 1 7a6 6 0 0 1 6-6z" fill="#7b3b76"/><circle cx="7" cy="7" r="2" fill="#2a0f28"/></svg>
    <div>Location name will be<br>here near this building 12345</div>
  </div>
  <div class="contact" style="left:470px">
    <svg width="15" height="12" viewBox="0 0 15 12"><rect x="0" y="0" width="15" height="11" rx="1.5" fill="#7b3b76"/><path d="M1 1l6.5 5L14 1" stroke="#2a0f28" fill="none"/></svg>
    <div><span class="lbl">Email us</span><br><span style="margin-left:4px">hello@lumoraworks.example</span></div>
  </div>
  <div class="contact" style="left:705px">
    <svg width="14" height="14" viewBox="0 0 14 14"><path d="M3 1l3 3-1.5 2a8 8 0 0 0 3.5 3.5L10 8l3 3-2 2C5 13 1 9 1 3z" fill="#7b3b76"/></svg>
    <div><span class="lbl">Call us</span><br>+1 555-010-4821</div>
  </div>
  <div class="social" style="top:92px" aria-label="Video channel"></div>
  <div class="social" style="top:128px" aria-label="Short posts"></div>
  <div class="social" style="top:163px" aria-label="Social page"></div>
  <div class="foot-brand">lumoraworks</div>
  <div class="foot-link" style="left:436px">PRIVACY</div>
  <div class="foot-link" style="left:544px">TERMS</div>
  <div class="foot-link" style="left:641px">DISCLAIMER</div>
  <div class="foot-link" style="left:771px">CONTACT US</div>
  <div class="copy">© 2024 Lumora Works, LLC. All Rights Reserved.</div>
</footer>

</body>
</html>
```